Business Card Design

Mortgage brokering company, also providing Commercial Finance, Car Finance and Insurance.

Target Market(s)

Home Buyers

Industry/Entity Type

Business

Contact Information for Business Card

All information required on business card is contained in the attachment. Design does not have to follow the style of the attachment.

```html
<!DOCTYPE html>
<html lang="en">
<head>
<meta charset="utf-8">
<title>Kestrel Home Loans – Business Card</title>
<link rel="stylesheet" href="https://fonts.googleapis.com/css2?family=Arimo:wght@400;700&display=swap">
<style>
  :root {
    --page: #e9e6e1;
    --card-dark: #1b1b1c;
    --card-dark-edge: #2a2a2c;
    --card-light: #ffffff;
    --orange: #f28a1e;
    --orange-deep: #e85a1a;
    --orange-light: #f8b33a;
    --ink: #2b2b2b;
    --text-light: #f4f4f4;
  }
  * { margin: 0; padding: 0; box-sizing: border-box; }
  html, body {
    width: 1200px; height: 784px; overflow: hidden;
    background: var(--page);
    font-family: "Arimo", Arial, sans-serif;
  }
  .canvas { position: relative; width: 1200px; height: 784px; }

  .card {
    position: absolute; width: 560px; height: 320px;
    border-radius: 3px; overflow: hidden;
    box-shadow: 0 8px 22px rgba(0,0,0,.18);
    background: radial-gradient(ellipse at 30% 20%, var(--card-dark-edge), var(--card-dark) 70%);
  }
  .card--front { left: 60px; top: 80px; }
  .card--back  { left: 590px; top: 390px; }

  /* front */
  .front-header {
    position: absolute; left: 0; top: 0; width: 100%; height: 118px;
    background: var(--card-light);
  }
  .front-rule {
    position: absolute; left: 0; top: 118px; width: 100%; height: 8px;
    background: linear-gradient(90deg, var(--orange-deep), var(--orange) 50%, var(--orange-light));
  }
  .brand {
    position: absolute; left: 30px; top: 58px;
    display: flex; align-items: center; gap: 16px;
  }
  .brand-dot {
    width: 46px; height: 46px; border-radius: 50%;
    background: var(--orange);
  }
  .brand-name { font-size: 25px; color: var(--ink); font-weight: 400; }
  .person {
    position: absolute; right: 26px; top: 16px; text-align: right;
  }
  .person-name { font-size: 14px; color: var(--orange); }
  .person-role { font-size: 10.5px; color: var(--ink); margin-top: 2px; }

  .contacts {
    position: absolute; left: 30px; top: 144px; list-style: none;
    color: var(--text-light); font-size: 16px; line-height: 1.1;
  }
  .contacts li { display: flex; align-items: flex-start; gap: 8px; margin-bottom: 5px; }
  .contacts svg { width: 16px; height: 16px; flex: none; margin-top: 1px; }
  .contacts .indent { padding-left: 24px; margin-top: -3px; }

  /* back */
  .services {
    position: absolute; left: 40px; top: 72px;
    display: grid; grid-template-columns: 128px auto; row-gap: 6px;
    font-size: 17px;
  }
  .service-label { color: var(--orange); }
  .service-items { color: var(--text-light); font-size: 15.5px; padding-top: 1px; }
  .mark-circle {
    position: absolute; right: 36px; top: 150px;
    width: 150px; height: 150px; border-radius: 50%;
    background: radial-gradient(circle at 60% 60%, var(--orange-light), var(--orange) 55%, var(--orange-deep));
  }
</style>
</head>
<body>
<main class="canvas">

  <section class="card card--front" aria-label="Business card front">
    <div class="front-header"></div>
    <div class="front-rule"></div>

    <div class="person">
      <p class="person-name">Martin Hale</p>
      <p class="person-role">Credit Representative</p>
    </div>

    <div class="brand">
      <span class="brand-dot"></span>
      <span class="brand-name">Kestrel Home Loans</span>
    </div>

    <ul class="contacts">
      <li>
        <svg viewBox="0 0 16 16"><rect x="4" y="1" width="8" height="14" rx="1.5" fill="var(--orange)"/><rect x="5.5" y="3" width="5" height="8" fill="var(--card-dark)"/></svg>
        <span>0400 555 182</span>
      </li>
      <li>
        <svg viewBox="0 0 16 16"><path d="M2 5c0-2 2-3 6-3s6 1 6 3v1h-3V5H5v1H2z" fill="var(--orange)"/><rect x="3" y="8" width="10" height="6" rx="1" fill="var(--orange)"/></svg>
        <span>07 5550 2146</span>
      </li>
      <li>
        <svg viewBox="0 0 16 16"><path d="M8 1l7 7h-2v7H9v-4H7v4H3V8H1z" fill="var(--orange)"/></svg>
        <span>14 Harbour View Drive,</span>
      </li>
      <li class="indent"><span>Seabrook, Qld 4219</span></li>
      <li>
        <svg viewBox="0 0 16 16"><circle cx="8" cy="8" r="7" fill="var(--orange)"/><g fill="none" stroke="var(--card-dark)" stroke-width="1"><ellipse cx="8" cy="8" rx="3" ry="7"/><path d="M1 8h14M2.5 4.5h11M2.5 11.5h11"/></g></svg>
        <span>www.kestrelhomeloans.com.au</span>
      </li>
      <li>
        <svg viewBox="0 0 16 16"><rect x="1" y="3" width="14" height="10" rx="1" fill="var(--orange)"/><path d="M1.5 3.5L8 9l6.5-5.5" fill="none" stroke="var(--card-dark)" stroke-width="1.2"/></svg>
        <span>martin.hale@kestrelhomeloans.com.au</span>
      </li>
    </ul>
  </section>

  <section class="card card--back" aria-label="Business card back">
    <div class="services">
      <span class="service-label">Residential</span>
      <span class="service-items">– First Home, Refinance, Investment</span>
      <span class="service-label">Asset Finance</span>
      <span class="service-items">– Plant and Equipment, Motor Vehicle</span>
      <span class="service-label">Insurance</span>
      <span class="service-items">– Home, Contents, Car</span>
    </div>
    <span class="mark-circle"></span>
  </section>

</main>
</body>
</html>
```